Wholesale company needs a sales brochure for our latest gadget- Nimbo Pebble. We sell to retailers

We need a sale brochure for our new product- Nimbo/Dart Pebble. It's an elegant little device that connects to any smartphone using an APP and let you locate your keys or your phone when you can't find them. We would like to see a design that uses the colors: Light blue, Black and metallic silver. The final design should communicate tech and innovative product. We need a total of 4 pages of 8.5x11'' (US letter size) to describe:
- Product benefits
- Product in use
- Display solution
- Profit generator
- Success story

Attached below are photos of the packaging and the display for your reference. Better photos will be sent later.
Please keep in mind that this product should be displayed on the counter with high foot traffic OR hang on hooks on a display fixture in the store.

This brochure will be used mainly to be sent digitally via email BUT we will also print it and will be mailing copies to our buyers.

Target Market(s)

Retailers and Distributors.
Small to mid-size retail stores:
- Electronic stores
- Convenient store
- Cellphone stores
- Gift stores

Industry/Entity Type

Retail

Font styles to use
Sans Serif

Colors
0692cd
ffffff
f3f1f8
33a6d7
85cae6

Requirements
Must have
• Must have:
• - "techie" and innovative look to go hand in hand with the product itself.
• - "in use" photos
• - "Description of the product"
• - Spec info
Nice to have
• Pattern or abstract design on background behind the text and images

```html
<!DOCTYPE html>
<html lang="en">
<head>
<meta charset="utf-8">
<title>Nimbo/Dart Pebble – Sales Brochure</title>
<link href="https://fonts.googleapis.com/css2?family=Poppins:wght@600;700;800&family=Open+Sans:wght@400;600;700&display=swap" rel="stylesheet">
<style>
  :root {
    --stage: #2f2f2f;
    --paper: #ffffff;
    --ink: #111111;
    --blue: #0692cd;
    --blue-mid: #33a6d7;
    --blue-light: #85cae6;
    --band-blue: #3a8fb5;
    --pattern: #f3f1f8;
    --text: #222222;
    --silver: #c9ccd1;
  }
  * { margin: 0; padding: 0; box-sizing: border-box; }
  html, body { width: 1200px; height: 900px; overflow: hidden; }
  body {
    position: relative;
    background: var(--stage);
    font-family: "Open Sans", Arial, sans-serif;
    color: var(--text);
  }
  .page { position: absolute; top: 110px; width: 538px; height: 696px; background: var(--paper); overflow: hidden; }
  .page--front { left: 54px; }
  .page--inside { left: 624px; width: 537px; }

  .abs { position: absolute; }

  /* front page */
  .front__pattern {
    left: 0; top: 195px; width: 538px; height: 475px;
    background: linear-gradient(135deg, #f7f7f9 0%, #ececf0 50%, #f7f7f9 100%);
  }
  .front__rule-top { left: 0; top: 68px; width: 538px; height: 5px; background: var(--blue-mid); }
  .front__masthead { left: 0; top: 80px; width: 538px; height: 110px; background: var(--ink); }
  .front__rule-bottom { left: 0; top: 190px; width: 538px; height: 5px; background: var(--blue-mid); }
  .brand-name {
    left: 44px; top: 86px;
    font-family: "Poppins", Arial, sans-serif; font-weight: 700;
    font-size: 76px; line-height: 1; color: var(--paper); letter-spacing: -1px;
  }
  .hero-photo {
    left: 330px; top: 115px; width: 208px; height: 540px;
    background: linear-gradient(180deg, var(--blue-light) 0%, var(--blue-mid) 18%, #dfe2e6 30%, #a9adb3 70%, #eceef0 100%);
    clip-path: polygon(0 0, 100% 0, 100% 100%, 10% 100%, 5% 40%);
  }
  .headline-top {
    left: 38px; top: 214px;
    font-family: "Poppins", Arial, sans-serif; font-weight: 700;
    font-size: 41px; line-height: 1; color: var(--blue); letter-spacing: 0;
  }
  .headline-main {
    left: 36px; top: 266px;
    font-family: "Poppins", Arial, sans-serif; font-weight: 800;
    font-size: 70px; line-height: 1; color: var(--ink); letter-spacing: -2px;
  }
  .intro {
    left: 38px; top: 353px; width: 300px;
    font-size: 9.6px; font-weight: 600; line-height: 1.35; color: var(--ink);
  }
  .product-frame {
    left: 46px; top: 406px; width: 246px; height: 106px;
    border: 4px solid var(--blue-mid); border-radius: 14px; overflow: hidden;
    background: linear-gradient(90deg, #d9d9dc 0%, #e8e3e4 33%, #c9cacc 50%, #ecedef 70%, #d8d9db 100%);
  }
  .section-label {
    left: 45px; top: 534px;
    font-family: "Poppins", Arial, sans-serif; font-weight: 700;
    font-size: 17px; line-height: 1; color: var(--blue);
  }
  .section-label .bracket { color: var(--ink); font-weight: 600; font-size: 22px; }
  .front__copy {
    left: 46px; top: 566px; width: 466px;
    font-size: 7.6px; line-height: 1.4; text-align: justify; color: var(--ink);
  }
  .front__foot-line { left: 0; top: 675px; width: 538px; height: 3px; background: var(--ink); }
  .front__foot-band { left: 0; top: 682px; width: 538px; height: 14px; background: var(--band-blue); }

  /* inside page */
  .use-strip { left: 4px; top: 42px; width: 533px; height: 184px; display: flex; gap: 3px; }
  .use-photo { flex: 1; }
  .use-photo--red { background: linear-gradient(180deg, #e6e7ea 0%, #e8a4b0 35%, #b9bcc1 75%, #dcdee1 100%); }
  .use-photo--black { background: linear-gradient(180deg, #e6e7ea 0%, #3a3a3c 35%, #b0b3b8 75%, #dcdee1 100%); }
  .use-photo--white { background: linear-gradient(180deg, #e6e7ea 0%, #f6f6f7 35%, #b9bcc1 75%, #dcdee1 100%); }

  .pill {
    height: 26px; border-radius: 0 13px 13px 0;
    font-family: "Poppins", Arial, sans-serif; font-weight: 700;
    color: var(--paper); line-height: 26px;
  }
  .pill--blue { background: var(--blue-mid); }
  .pill--black { background: var(--ink); }
  .pill--use { left: 0; top: 260px; width: 212px; padding-left: 36px; font-size: 18px; }
  .pill--display { left: 0; top: 375px; width: 212px; padding-left: 29px; font-size: 18px; }
  .pill--web { left: 0; top: 612px; width: 249px; padding-left: 4px; font-size: 14px; font-weight: 600; }

  .inside__copy { font-size: 7.6px; line-height: 1.4; text-align: justify; color: var(--ink); }
  .inside__copy--use { left: 26px; top: 296px; width: 476px; }
  .inside__copy--display-a { left: 26px; top: 410px; width: 296px; }
  .inside__copy--display-b { left: 26px; top: 513px; width: 296px; }

  .display-photo {
    left: 356px; top: 368px; width: 140px; height: 294px;
    background: linear-gradient(180deg, #f4f4f5 0%, #e9eaec 18%, #1c1c1e 30%, #2a3d4f 55%, #1c1c1e 90%, #0f0f10 100%);
  }
</style>
</head>
<body>

<section class="page page--front">
  <div class="abs front__pattern" role="img" aria-label="Soft geometric hexagon pattern in light grey"></div>
  <div class="abs front__rule-top"></div>
  <div class="abs front__masthead"></div>
  <div class="abs front__rule-bottom"></div>
  <div class="abs brand-name">Nimbo</div>

  <div class="abs hero-photo" role="img" aria-label="Photo of a light blue triangular Nimbo Pebble tag on a ring with silver keys"></div>

  <h1 class="abs headline-top">NIMBO/DART</h1>
  <div class="abs headline-main">PEBBLE</div>

  <p class="abs intro">Nimbo/Dart Pebble. It's an elegant little device that connects to any smartphone using an APP and let you locate your keys or your phone when you can't find them.</p>

  <div class="abs product-frame" role="img" aria-label="Photo of three packaged Nimbo Pebble tags in red, black and white with keys"></div>

  <h2 class="abs section-label"><span class="bracket">[</span> PRODUCT BENEFITS <span class="bracket">]</span></h2>
  <p class="abs front__copy">Lorem Ipsum is simply dummy text of the printing and typesetting industry. Lorem Ipsum has been the industry's standard dummy text ever since the 1500s, when an unknown printer took a galley of type and scrambled it to make a type specimen book. It has survived not only five centuries, but also the leap into electronic typesetting, remaining essentially unchanged. It was popularised in the 1960s with the release of Lettrafix sheets containing Lorem Ipsum passages, and more recently with desktop publishing software like Folio Layout including versions of Lorem Ipsum.</p>

  <div class="abs front__foot-line"></div>
  <div class="abs front__foot-band"></div>
</section>

<section class="page page--inside">
  <div class="abs use-strip">
    <div class="use-photo use-photo--red" role="img" aria-label="Photo of a red Nimbo Pebble tag on keys in its package card"></div>
    <div class="use-photo use-photo--black" role="img" aria-label="Photo of a black Nimbo Pebble tag on keys in its package card"></div>
    <div class="use-photo use-photo--white" role="img" aria-label="Photo of a white Nimbo Pebble tag on keys in its package card"></div>
  </div>

  <h2 class="abs pill pill--blue pill--use">Product in use</h2>
  <p class="abs inside__copy inside__copy--use">Lorem Ipsum is simply dummy text of the printing and typesetting industry. Lorem Ipsum has been the industry's standard dummy text ever since the 1500s, when an unknown printer took a galley of type and scrambled it to make a type specimen book. It has survived not only five centuries, but also the leap into electronic typesetting, remaining essentially unchanged. It was popularised in the 1960s with the release of Lettrafix sheets containing Lorem Ipsum passages, and more recently with desktop publishing software like Folio Layout including versions of Lorem Ipsum.</p>

  <h2 class="abs pill pill--black pill--display">Display solution</h2>
  <p class="abs inside__copy inside__copy--display-a">Lorem Ipsum is simply dummy text of the printing and typesetting industry. Lorem Ipsum has been the industry's standard dummy text ever since the 1500s, when an unknown printer took a galley of type and scrambled it to make a type specimen book. It has survived not only five centuries, but also the leap into electronic typesetting, remaining essentially unchanged. It was popularised in the 1960s with the release of Lettrafix sheets containing Lorem Ipsum passages, and more recently with desktop publishing software like Folio Layout including versions of Lorem Ipsum.</p>
  <p class="abs inside__copy inside__copy--display-b">Lorem Ipsum is simply dummy text of the printing and typesetting industry. Lorem Ipsum has been the industry's standard dummy text ever since the 1500s, when an unknown printer took a galley of type and scrambled it to make a type specimen book. It has survived not only five centuries, but also the leap into electronic typesetting, remaining essentially unchanged. It was popularised in the 1960s with the release of Lettrafix sheets containing Lorem Ipsum passages, and more recently with desktop publishing software like Folio Layout including versions of Lorem Ipsum.</p>

  <div class="abs pill pill--blue pill--web">visit-www.nimbopebble.com</div>

  <div class="abs display-photo" role="img" aria-label="Photo of a black counter display box holding six packaged Nimbo Pebble tags"></div>
</section>

</body>
</html>
```